Maple Lantern Business Card

Design of business cards

Target Market(s)

We are aiming as small business owners who need anything from basic business structures, website plans, business processes and quality assurance.

Industry/Entity Type

Business

Colors

Designer to choose colors to be used in the design.

Requirements
Nice to have
• I would prefer one side of the card to use the green from the logo. Prefer to have the same font as the logo.

```html
<!DOCTYPE html>
<html lang="en">
<head>
<meta charset="utf-8">
<title>Maple Lantern Business Cards</title>
<link rel="stylesheet" href="https://fonts.googleapis.com/css2?family=Cinzel:wght@400;600&display=swap">
<style>
  :root {
    --leaf: #9bc53d;
    --charcoal: #4a4a4c;
    --paper: #fbfbfb;
    --paper-shade: #ececec;
    --frame: #d9d9d9;
    --ring: #dcdcdc;
    --ink-light: #ffffff;
  }
  * { margin: 0; padding: 0; box-sizing: border-box; }
  html, body { width: 788px; height: 1200px; overflow: hidden; }
  body {
    background: #ffffff;
    font-family: "Cinzel", serif;
    position: relative;
  }
  .card {
    position: absolute;
    left: 48px;
    width: 692px;
    height: 352px;
    border: 2px solid var(--frame);
    overflow: hidden;
    background: linear-gradient(180deg, var(--paper) 0%, var(--paper-shade) 100%);
  }
  .card--front { top: 26px; }
  .card--back-plain { top: 418px; }
  .card--back-accent { top: 806px; }

  .accent-ring {
    position: absolute;
    border-radius: 50%;
    background: var(--ring);
    opacity: 0.6;
  }
  .card--front .accent-ring { right: -20px; top: 100px; width: 170px; height: 170px; }
  .card--back-accent .accent-ring { right: 60px; top: 18px; width: 104px; height: 104px; }

  .brand {
    position: absolute;
    display: flex;
    align-items: center;
    gap: 16px;
    color: var(--leaf);
    z-index: 1;
  }
  .brand__dot {
    width: 44px; height: 44px;
    border-radius: 50%;
    background: var(--leaf);
    flex: none;
  }
  .brand__name {
    font-weight: 600;
    font-size: 28px;
    line-height: 1.1;
    letter-spacing: 1px;
    white-space: nowrap;
  }
  .card--front .brand { left: 150px; top: 92px; }
  .card--back-plain .brand,
  .card--back-accent .brand { left: 178px; top: 28px; }
  .card--back-plain .brand__name,
  .card--back-accent .brand__name { font-size: 24px; }
  .card--back-plain .brand__dot,
  .card--back-accent .brand__dot { width: 38px; height: 38px; }

  .contact-bar {
    position: absolute;
    left: 0; right: 0; bottom: 0;
    height: 72px;
    display: flex;
    align-items: center;
    padding: 0 28px;
    color: var(--ink-light);
    font-size: 15px;
    letter-spacing: 0.5px;
    z-index: 1;
  }
  .card--front .contact-bar {
    background: var(--charcoal);
    border-top: 6px solid var(--leaf);
  }
  .contact-bar__phone { display: flex; align-items: center; gap: 10px; width: 210px; }
  .contact-bar__phone svg { width: 22px; height: 22px; }

  .name-panel {
    position: absolute;
    left: 0; right: 0; bottom: 0;
    height: 212px;
    background: var(--leaf);
  }
  .name-panel__name {
    position: absolute;
    left: 0; right: 0; top: 58px;
    text-align: center;
    color: var(--ink-light);
    font-size: 40px;
    font-weight: 400;
    letter-spacing: 2px;
  }
  .name-panel .contact-bar { background: transparent; }
</style>
</head>
<body>

  <section class="card card--front">
    <div class="accent-ring"></div>
    <div class="brand">
      <span class="brand__dot"></span>
      <span class="brand__name">Maple Lantern<br>Consulting</span>
    </div>
    <div class="contact-bar">
      <span class="contact-bar__phone">
        <svg viewBox="0 0 24 24" aria-hidden="true">
          <circle cx="12" cy="12" r="10.5" fill="none" stroke="#fff" stroke-width="1.6"/>
          <path d="M8.6 6.8l1.9-.4 1.1 2.7-1.3 1c.6 1.3 1.6 2.3 2.9 2.9l1-1.3 2.7 1.1-.4 1.9c-4.2.2-8.1-3.7-7.9-7.9z" fill="#fff"/>
        </svg>
        0400 555 127
      </span>
      <span class="contact-bar__web">www.maplelantern.com.au</span>
    </div>
  </section>

  <section class="card card--back-plain">
    <div class="brand">
      <span class="brand__dot"></span>
      <span class="brand__name">Maple Lantern<br>Consulting</span>
    </div>
    <div class="name-panel">
      <h1 class="name-panel__name">Elena Marsh</h1>
      <div class="contact-bar">
        <span class="contact-bar__phone">
          <svg viewBox="0 0 24 24" aria-hidden="true">
            <circle cx="12" cy="12" r="10.5" fill="none" stroke="#fff" stroke-width="1.6"/>
            <path d="M8.6 6.8l1.9-.4 1.1 2.7-1.3 1c.6 1.3 1.6 2.3 2.9 2.9l1-1.3 2.7 1.1-.4 1.9c-4.2.2-8.1-3.7-7.9-7.9z" fill="#fff"/>
          </svg>
          0400 555 127
        </span>
        <span class="contact-bar__web">www.maplelantern.com.au</span>
      </div>
    </div>
  </section>

  <section class="card card--back-accent">
    <div class="accent-ring"></div>
    <div class="brand">
      <span class="brand__dot"></span>
      <span class="brand__name">Maple Lantern<br>Consulting</span>
    </div>
    <div class="name-panel">
      <h1 class="name-panel__name">Elena Marsh</h1>
      <div class="contact-bar">
        <span class="contact-bar__phone">
          <svg viewBox="0 0 24 24" aria-hidden="true">
            <circle cx="12" cy="12" r="10.5" fill="none" stroke="#fff" stroke-width="1.6"/>
            <path d="M8.6 6.8l1.9-.4 1.1 2.7-1.3 1c.6 1.3 1.6 2.3 2.9 2.9l1-1.3 2.7 1.1-.4 1.9c-4.2.2-8.1-3.7-7.9-7.9z" fill="#fff"/>
          </svg>
          0400 555 127
        </span>
        <span class="contact-bar__web">www.maplelantern.com.au</span>
      </div>
    </div>
  </section>

</body>
</html>
```